Envelope Design Project for Real Estate

I am looking for an envelope design for a real estate brokerage. I prefer muted colors and the primary colors should be white, maroon (884445) and gray (aaaaaa).
The design is for a #10 universal envelope (psd and jpg files attached for guidelines). There should be full color on the front and back of the envelope.
You can add a return address on the back side along the top flap. Please use a sample address and phone number in the design - the actual information will be provided to the winning designer.
Industry/Entity Type
Real Estate
Look and feel
Each slider illustrates characteristics of the customer's brand and the style your logo design should communicate.

```html
<!DOCTYPE html>
<html lang="en">
<head>
<meta charset="utf-8">
<title>Oak Harbor Realty – #10 Envelope</title>
<link rel="stylesheet" href="https://fonts.googleapis.com/css2?family=Cinzel:wght@400;600&family=Cormorant+Garamond:ital,wght@1,600&display=swap">
<style>
  :root {
    --backdrop: #a87a22;
    --maroon: #884445;
    --maroon-deep: #6c3233;
    --gray: #aaaaaa;
    --tab-gray: #9a9a9a;
    --paper: #ffffff;
    --guide: #6fcf5f;
    --faint: #efefef;
    --ink: #2b2b2b;
  }
  html, body {
    margin: 0;
    padding: 0;
    width: 1200px;
    height: 686px;
    overflow: hidden;
    background: var(--backdrop);
  }
  .envelope-dieline {
    display: block;
    width: 1200px;
    height: 686px;
  }
  .brand-name { font-family: "Cinzel", serif; font-weight: 400; fill: var(--maroon); }
  .brand-name--reverse { fill: var(--paper); }
  .address-line { font-family: "Cinzel", serif; font-size: 8.5px; fill: var(--ink); }
  .address-line--reverse { fill: #f3e6e6; font-size: 9px; }
  .mobile-label { font-family: "Cormorant Garamond", serif; font-style: italic; font-weight: 600; fill: var(--maroon); font-size: 10px; }
  .web-line { font-family: "Cinzel", serif; font-size: 7.5px; fill: var(--paper); }
  .guide { fill: none; stroke: var(--guide); stroke-width: 0.8; }
  .cut-line { fill: none; stroke: var(--paper); stroke-width: 1.2; stroke-dasharray: 5 3; }
</style>
</head>
<body>
<svg class="envelope-dieline" viewBox="0 0 1190 680" preserveAspectRatio="none" xmlns="http://www.w3.org/2000/svg">
  <defs>
    <linearGradient id="maroon-band" x1="0" x2="1" y1="0" y2="0">
      <stop offset="0" stop-color="var(--maroon-deep)"/>
      <stop offset="0.3" stop-color="var(--maroon)"/>
      <stop offset="0.7" stop-color="var(--maroon)"/>
      <stop offset="1" stop-color="var(--maroon-deep)"/>
    </linearGradient>
    <linearGradient id="gray-swoosh" x1="0" x2="1" y1="0" y2="0">
      <stop offset="0" stop-color="#555"/>
      <stop offset="0.6" stop-color="var(--gray)"/>
      <stop offset="1" stop-color="#e6e6e6"/>
    </linearGradient>
  </defs>

  <!-- cut outline -->
  <path class="cut-line" d="M274,148 L292,70 Q297,52 316,52 L854,52 Q872,52 875,70 L880,140 L915,140 Q936,140 936,160 L936,380 Q936,395 915,400 L880,408 L875,615 Q872,638 850,640 L300,640 Q280,638 280,615 L276,408 L240,400 Q218,395 218,380 L218,160 Q218,140 240,140 Z"/>

  <!-- top flap -->
  <g class="top-flap">
    <path fill="url(#maroon-band)" d="M282,148 L300,76 Q304,62 320,62 L850,62 Q864,62 866,76 L872,148 Z"/>
    <path class="guide" d="M298,134 L312,74 L842,74 L856,134 Z"/>
    <text class="address-line address-line--reverse" text-anchor="middle" transform="translate(578,106) rotate(180)">Complex name,Street name City, State, zip code</text>
  </g>

  <!-- side flaps -->
  <g class="side-flaps">
    <path fill="var(--paper)" d="M282,148 L282,400 L240,392 Q228,390 228,378 L228,168 Q228,150 246,150 Z"/>
    <path fill="var(--tab-gray)" d="M232,195 L254,195 Q260,195 260,201 L262,395 L240,390 Q222,385 220,370 L220,205 Q220,195 232,195 Z"/>
    <path fill="var(--paper)" d="M872,148 L872,400 L912,392 Q924,390 924,378 L924,168 Q924,150 906,150 Z"/>
    <path fill="var(--tab-gray)" d="M922,195 L900,195 Q894,195 894,201 L888,395 L912,390 Q932,385 934,370 L934,205 Q934,195 922,195 Z"/>
  </g>

  <!-- front panel -->
  <g class="front-panel">
    <rect x="282" y="148" width="590" height="252" fill="var(--paper)"/>
    <circle cx="752" cy="290" r="96" fill="var(--faint)" role="img" aria-label="Faint brand emblem decoration"/>
    <path fill="url(#gray-swoosh)" d="M282,322 Q430,372 800,378 Q520,386 282,344 Z"/>
    <path fill="url(#maroon-band)" d="M282,346 Q520,392 860,352 L872,400 L282,400 Z"/>
    <path fill="var(--paper)" d="M724,400 L800,372 L812,372 L738,400 Z"/>
    <rect class="guide" x="294" y="158" width="564" height="230"/>

    <circle cx="381" cy="190" r="14" fill="var(--maroon)"/>
    <text class="brand-name" x="381" y="248" font-size="25" text-anchor="middle">Oak Harbor</text>
    <text class="brand-name" x="381" y="263" font-size="10" letter-spacing="3" text-anchor="middle">REALTY</text>

    <text class="address-line" x="378" y="288" text-anchor="middle">Complex name,Street name</text>
    <text class="address-line" x="378" y="298" text-anchor="middle">City, State, zip code</text>
    <text x="378" y="316" text-anchor="middle"><tspan class="mobile-label">Mobile :</tspan><tspan class="address-line"> (555) 014-2837</tspan></text>

    <text class="web-line" x="300" y="384">www.HarborHomeFinderBlog.com</text>
  </g>

  <!-- bottom flap -->
  <g class="bottom-flap">
    <path fill="url(#maroon-band)" d="M282,400 L872,400 L862,604 Q860,624 842,624 L306,624 Q290,624 290,604 Z"/>
    <path class="guide" d="M298,414 L856,414 L850,556 L302,556 Z"/>
    <text class="brand-name brand-name--reverse" x="564" y="431" font-size="10" letter-spacing="3" text-anchor="middle" transform="rotate(180 564 431)">REALTY</text>
    <text class="brand-name brand-name--reverse" x="564" y="446" font-size="25" text-anchor="middle" transform="rotate(180 564 446)">Oak Harbor</text>
    <circle cx="564" cy="500" r="14" fill="var(--paper)"/>
    <path fill="var(--tab-gray)" d="M322,578 L832,578 Q840,578 842,586 L852,632 L302,632 L314,586 Q316,578 322,578 Z"/>
  </g>
</svg>
</body>
</html>
```